PawHush business card

Looking for a fun and cool biz card for a new company with patent pending products. I have products to help and protect dogs hearing. My colors are pantone blue and orange.
Updates

Please add tag line: Protect the ones you love...even your PawHushes!

Target Market(s)

Animal/Dog lovers!

Industry/Entity Type

Retail

Contact Information for Business Card

I'm looking for something simple yet fun with all the info included for biz cards

Colors
0555a3
f78f20

Requirements
Must have
• Logo
Nice to have
• name, website and email
Should not have
• phone number

```html
<!DOCTYPE html>
<html lang="en">
<head>
<meta charset="utf-8">
<title>PawHush business card</title>
<link rel="stylesheet" href="https://fonts.googleapis.com/css2?family=Roboto:wght@400;500;700;900&family=Roboto+Condensed:wght@500;700&display=swap">
<style>
  :root {
    --brand-blue: #0a2e8c;
    --brand-orange: #ff5200;
    --paper: #f2f2f2;
    --ink-grey: #4a4a4a;
    --backdrop: #2b2b2b;
    --white: #ffffff;
  }
  html, body {
    margin: 0;
    padding: 0;
    width: 1200px;
    height: 960px;
    overflow: hidden;
    background: var(--backdrop);
  }
  .canvas {
    position: relative;
    width: 1200px;
    height: 960px;
    font-family: "Roboto", Arial, sans-serif;
  }
  .card {
    position: absolute;
    left: 320px;
    width: 600px;
    height: 342px;
    box-sizing: border-box;
  }
  /* Front */
  .card-front {
    top: 102px;
    background: var(--brand-blue);
  }
  .front-wordmark {
    position: absolute;
    left: 0;
    right: 0;
    top: 140px;
    display: flex;
    align-items: center;
    justify-content: center;
    gap: 14px;
  }
  .front-wordmark .mark-dot {
    width: 34px;
    height: 34px;
    border-radius: 50%;
    background: var(--brand-orange);
  }
  .front-wordmark .mark-name {
    font-weight: 900;
    font-size: 54px;
    line-height: 60px;
    color: var(--brand-orange);
    letter-spacing: 0.5px;
  }
  .front-url {
    position: absolute;
    left: 0;
    right: 0;
    top: 303px;
    text-align: center;
    color: var(--white);
    font-size: 14px;
    letter-spacing: 5.5px;
  }
  /* Back */
  .card-back {
    top: 493px;
    background: var(--paper);
  }
  .side-band {
    position: absolute;
    left: 0;
    top: 0;
    width: 65px;
    height: 100%;
    background: var(--brand-orange);
  }
  .back-wordmark {
    position: absolute;
    left: 30px;
    top: 46px;
    display: flex;
    align-items: center;
    gap: 10px;
  }
  .back-wordmark .mark-dot {
    width: 22px;
    height: 22px;
    border-radius: 50%;
    background: var(--brand-blue);
  }
  .back-wordmark .mark-name {
    font-weight: 900;
    font-size: 44px;
    line-height: 50px;
    color: var(--brand-blue);
  }
  .tagline {
    position: absolute;
    left: 95px;
    top: 104px;
    font-size: 13px;
    line-height: 16px;
    font-weight: 500;
    color: var(--brand-blue);
  }
  .contact {
    position: absolute;
    right: 30px;
    top: 155px;
    text-align: right;
    color: var(--ink-grey);
    font-size: 14.5px;
    line-height: 19px;
  }
  .person-name {
    font-family: "Roboto Condensed", Arial, sans-serif;
    font-weight: 700;
    font-size: 21px;
    line-height: 24px;
    color: var(--brand-orange);
  }
  .person-role {
    font-family: "Roboto Condensed", Arial, sans-serif;
    font-weight: 700;
    font-size: 15px;
    line-height: 18px;
    color: var(--brand-blue);
    margin-bottom: 12px;
  }
  .address { margin-bottom: 8px; }
  .contact-line {
    display: flex;
    justify-content: flex-end;
    align-items: center;
    gap: 8px;
  }
  .contact-line svg {
    width: 12px;
    height: 12px;
    fill: var(--brand-orange);
    flex: none;
  }
</style>
</head>
<body>
<main class="canvas">
  <section class="card card-front" aria-label="Card front">
    <div class="front-wordmark">
      <span class="mark-dot"></span>
      <span class="mark-name">PawHush</span>
    </div>
    <div class="front-url">www.pawhush.com</div>
  </section>

  <section class="card card-back" aria-label="Card back">
    <div class="side-band"></div>
    <div class="back-wordmark">
      <span class="mark-dot"></span>
      <span class="mark-name">PawHush</span>
    </div>
    <p class="tagline" style="margin:0">Protect the ones you love...even your PawHushes!</p>
    <div class="contact">
      <div class="person-name">DANA WELLS</div>
      <div class="person-role">CEO/FOUNDER</div>
      <div class="address">214 Birchwood Road<br>Juneau, Alaska 99801</div>
      <div class="contact-line">dana@pawhush.com
        <svg viewBox="0 0 24 24" aria-hidden="true"><path d="M2 5h20v14H2z M2 5l10 8 10-8" stroke="#f2f2f2" stroke-width="1.6"/></svg>
      </div>
      <div class="contact-line">www.pawhush.com
        <svg viewBox="0 0 24 24" aria-hidden="true"><circle cx="12" cy="12" r="10"/><path d="M2 12h20M12 2c3 3 3 17 0 20M12 2c-3 3-3 17 0 20" stroke="#f2f2f2" stroke-width="1.5" fill="none"/></svg>
      </div>
    </div>
  </section>
</main>
</body>
</html>
```